Social Media Graphics - Harbor Climb REVISED

Create 6-7 individual social media graphics (square size) to encourage folks to join our online course called:

The Lantern Ledger Plan
How to Launch a Multi-Million Business From Scratch
Sign Up Today!

IMPORTANT: Make the largest and most prominent text on the graphic be: How to Launch a Multi-Million Business From Scratch

For the color scheme of the graphics, let's try a blue color palette; make sure the graphics appeal to both men and women

Make sure each graphic contains 1 of the 3 pics attached (crop pic as needed); and make sure one of the graphics is all TEXT only.

Target Market(s)

men and women looking to start a business

Industry/Entity Type

Entrepreneurship

Colors
0054AA
0677BA
7BADD7
CADEEF
E8F1F8

Requirements
Must have
• All the text and use the 3 pics provided; one graphic can be all text; Simple, modern design that's easy to read

```html
<!DOCTYPE html>
<html lang="en">
<head>
<meta charset="utf-8">
<title>The Lantern Ledger Plan – Social Graphics</title>
<link rel="stylesheet" href="https://fonts.googleapis.com/css2?family=Bebas+Neue&display=swap">
<style>
  :root {
    --stage: #8f8f8f;
    --blue-deep: #0054aa;
    --blue-mid: #0677ba;
    --blue-bright: #1c8fe0;
    --blue-soft: #7badd7;
    --blue-pale: #cadeef;
    --blue-mist: #e8f1f8;
    --ink: #111111;
    --white: #ffffff;
    --photo-dark: linear-gradient(160deg, #3a3f4d 0%, #1d2a55 55%, #25457f 100%);
    --photo-light: linear-gradient(160deg, #d8e6f3 0%, #b9cbe0 45%, #6b7a92 100%);
  }
  * { box-sizing: border-box; margin: 0; padding: 0; }
  html, body { width: 881px; height: 1200px; overflow: hidden; }
  body {
    background: var(--stage);
    position: relative;
    font-family: "Bebas Neue", "Arial Narrow", sans-serif;
  }
  .tile {
    position: absolute;
    width: 291px; height: 291px;
    overflow: hidden;
    background: var(--blue-deep);
  }
  .tile--glow { background: radial-gradient(circle at 65% 45%, var(--blue-bright) 0%, var(--blue-deep) 70%); }
  .tile svg.shape { position: absolute; inset: 0; width: 291px; height: 291px; }
  .txt { position: absolute; line-height: 1; white-space: nowrap; letter-spacing: 0.2px; z-index: 2; }
  .white { color: var(--white); }
  .blue { color: var(--blue-deep); }
  .ink { color: var(--ink); }
  .tag { padding: 1px 6px 0; }
  .tag--blue { background: var(--blue-deep); color: var(--white); }
  .tag--ink { background: var(--ink); color: var(--white); }
  .photo { position: absolute; z-index: 1; }
  .center { left: 0; width: 100%; text-align: center; }
  .pill { position: absolute; border-radius: 22px 22px 0 0; }
</style>
</head>
<body>

<!-- Tile 1 -->
<section class="tile" style="left:140px; top:132px;">
  <svg class="shape" viewBox="0 0 291 291">
    <path d="M12,0 C6,80 40,180 140,225 C190,246 240,252 291,254 V291 H0 V0 Z" fill="none" stroke="var(--white)" stroke-width="1.5"/>
    <path d="M15,0 H291 V249 C230,248 180,240 135,220 C50,180 10,100 15,0 Z" fill="var(--white)"/>
    <path d="M150,226 C200,244 250,248 291,250" stroke="var(--blue-deep)" stroke-width="3" fill="none"/>
  </svg>
  <div class="photo" role="img" aria-label="Photo of the two course hosts smiling, arms crossed" style="left:0; top:140px; width:165px; height:151px; background:var(--photo-dark); clip-path:path('M0,22 C8,6 24,0 44,0 C62,0 74,8 82,18 C92,14 108,18 116,32 C122,46 122,60 126,72 C142,92 156,118 165,151 H0 Z');"></div>
  <div class="txt blue" style="left:33px; top:22px; font-size:24px;">The Lantern <span class="tag tag--blue">Ledger Plan</span></div>
  <div class="txt ink" style="left:62px; top:66px; font-size:33px;">How to Launch a</div>
  <div class="txt ink" style="left:80px; top:100px; font-size:33px;">Multi-Million</div>
  <div class="txt blue" style="left:124px; top:136px; font-size:34px;">Business</div>
  <div class="txt ink" style="left:145px; top:178px; font-size:26px;">From Scratch</div>
  <div class="txt white" style="left:172px; top:265px; font-size:19px;">Sign Up Today!</div>
</section>

<!-- Tile 2 -->
<section class="tile tile--glow" style="left:454px; top:132px;">
  <svg class="shape" viewBox="0 0 291 291">
    <path d="M0,0 H110 C160,60 160,190 40,256 H0 Z" fill="var(--blue-pale)"/>
  </svg>
  <div class="photo" role="img" aria-label="Photo of the two hosts standing, one speaking into a microphone" style="left:0; top:30px; width:140px; height:226px; background:var(--photo-light); clip-path:path('M0,0 H105 C145,50 130,170 40,226 H0 Z');"></div>
  <div style="position:absolute; left:144px; top:12px; width:147px; height:75px; background:var(--white); border-radius:22px 0 0 22px;"></div>
  <div class="txt blue" style="left:163px; top:21px; font-size:28px;">The Lantern</div>
  <div class="txt blue" style="left:163px; top:52px; font-size:28px;">Ledger Plan</div>
  <div class="txt white" style="left:141px; top:141px; font-size:26px; line-height:1.06;">How to Launch<br>A Multi-Million<br>Business From<br>Scratch</div>
  <div class="pill" style="left:41px; top:264px; width:260px; height:30px; background:var(--blue-mid);"></div>
  <div class="txt white" style="left:104px; top:270px; font-size:19px;">Sign Up Today!</div>
</section>

<!-- Tile 3 -->
<section class="tile" style="left:140px; top:453px;">
  <svg class="shape" viewBox="0 0 291 291">
    <path d="M284,0 C292,110 255,200 150,226 C100,238 50,244 0,248 V0 Z" fill="var(--white)"/>
    <path d="M288,15 C292,110 262,205 155,232 C100,245 50,250 0,254" stroke="var(--blue-mid)" stroke-width="3" fill="none"/>
  </svg>
  <div class="photo" role="img" aria-label="Photo of the two hosts smiling, arms crossed" style="left:143px; top:120px; width:148px; height:171px; background:linear-gradient(160deg,#b23a55 0%,#7a2436 45%,#1e1e22 100%); border-radius:70px 60px 0 0;"></div>
  <div class="txt ink" style="left:16px; top:20px; font-size:26px;">The Lantern <span class="tag tag--ink">Ledger Plan</span></div>
  <div class="txt blue" style="left:17px; top:59px; font-size:34px; line-height:1.06;">How to Launch a<br>Multi-Million<br>Business</div>
  <div class="txt ink" style="left:17px; top:167px; font-size:34px; line-height:1.06;">From<br>Scratch</div>
  <div class="txt white" style="left:20px; top:264px; font-size:19px;">Sign Up Today!</div>
</section>

<!-- Tile 4 -->
<section class="tile" style="left:454px; top:454px;">
  <svg class="shape" viewBox="0 0 291 291">
    <path d="M58,162 C40,110 60,70 90,50" stroke="var(--blue-pale)" stroke-width="0.8" fill="none"/>
    <path d="M70,162 C58,115 72,80 100,60" stroke="var(--blue-pale)" stroke-width="0.8" fill="none"/>
    <path d="M238,162 C256,110 236,70 206,50" stroke="var(--blue-pale)" stroke-width="0.8" fill="none"/>
    <path d="M226,162 C238,115 224,80 196,60" stroke="var(--blue-pale)" stroke-width="0.8" fill="none"/>
    <line x1="0" y1="228" x2="80" y2="228" stroke="var(--blue-pale)" stroke-width="0.8"/>
    <line x1="212" y1="228" x2="291" y2="228" stroke="var(--blue-pale)" stroke-width="0.8"/>
  </svg>
  <div class="photo" role="img" aria-label="Circular photo of the two hosts smiling" style="left:73px; top:49px; width:152px; height:115px; background:var(--photo-dark); border-radius:76px 76px 0 0;"></div>
  <div class="txt white center" style="top:10px; font-size:29px;">The Lantern Ledger Plan</div>
  <div class="txt white center" style="top:164px; font-size:23px; line-height:1.15;">How to Launch a<br>Multi-Million Business<br>From Scratch</div>
  <div class="pill" style="left:30px; top:260px; width:231px; height:31px; background:var(--white);"></div>
  <div class="txt blue center" style="top:267px; font-size:20px;">Sign Up Today!</div>
</section>

<!-- Tile 5 -->
<section class="tile tile--glow" style="left:141px; top:770px;">
  <svg class="shape" viewBox="0 0 291 291">
    <path d="M170,0 H291 V255 C200,255 145,200 145,120 C145,60 155,25 170,0 Z" fill="var(--blue-pale)"/>
  </svg>
  <div class="photo" role="img" aria-label="Photo of the two hosts standing, one speaking into a microphone" style="left:120px; top:35px; width:171px; height:220px; background:var(--photo-light); clip-path:path('M40,0 H171 V220 C80,210 25,160 25,85 C25,45 30,20 40,0 Z');"></div>
  <div class="txt white" style="left:19px; top:22px; font-size:29px; line-height:1.06;">The Lantern<br>Ledger Plan</div>
  <div style="position:absolute; left:60px; top:87px; width:30px; height:1.5px; background:var(--white);"></div>
  <div class="txt white" style="left:17px; top:105px; font-size:26px; line-height:1.14;">How to<br>Launch a<br>Multi-Million<br>Business From<br>Scratch</div>
  <div class="pill" style="left:41px; top:264px; width:260px; height:30px; background:var(--white);"></div>
  <div class="txt blue" style="left:104px; top:270px; font-size:19px;">Sign Up Today!</div>
</section>

<!-- Tile 6: text only -->
<section class="tile" style="left:457px; top:776px; background:var(--white);">
  <div style="position:absolute; left:0; top:45px; width:291px; height:203px; background:radial-gradient(circle at 50% 45%, var(--blue-bright) 0%, var(--blue-deep) 75%);"></div>
  <div class="txt center" style="top:10px; font-size:29px;"><span class="blue">The Lantern</span> <span style="color:var(--blue-mid);">Ledger Plan</span></div>
  <div class="txt white center" style="top:63px; font-size:35px;">How to Launch a</div>
  <div class="txt white center" style="top:99px; font-size:44px;">Multi-Million</div>
  <div class="txt white center" style="top:147px; font-size:35px;">Business</div>
  <div class="txt white center" style="top:192px; font-size:35px;">From Scratch</div>
  <div class="txt blue center" style="top:255px; font-size:29px;">Sign Up Today!</div>
</section>

</body>
</html>
```